New business card design needed for Trucking/Staffing company!

I am looking for a business card design. The business name is Harbor Lane Freightworks, LLC. This company is a staffing company for commercial drivers/truck drivers. Most of our customers are trucking/supply companies. Our colors are blue/black/white/grey. The info I have on my current business cards is
-Spot for a name
-2 lines for an address
-3 lines for Office, cell, and fax
-email
-website(currently on backside of card with logo but can go anywhere)
Updates

Project Deadline Extended
Reason: Open to more designs

Target Market(s)

Trucking companies, building supply companies

Industry/Entity Type

Business

Contact Information for Business Card

Edgy but professional

Font styles to use
Other font styles liked:
• Open to suggestions

Colors
0555a3
000000
ffffff
9d9d9d

Requirements
Must have
• Must have the logo incorporated

```html
<!DOCTYPE html>
<html lang="en">
<head>
<meta charset="utf-8">
<title>Harbor Lane Freightworks – Business Card</title>
<link rel="stylesheet" href="https://fonts.googleapis.com/css2?family=Lato:wght@400;700;900&display=swap">
<style>
  :root {
    --stage: #d9d9d9;
    --card-black: #121316;
    --card-black-light: #26282c;
    --brand-blue: #3d52a6;
    --brand-blue-bright: #4a62c4;
    --white: #ffffff;
    --text-light: #e6e6e6;
    --grey: #9d9d9d;
  }
  * { box-sizing: border-box; margin: 0; padding: 0; }
  html, body {
    width: 1200px; height: 926px; overflow: hidden;
    background: var(--stage);
    font-family: "Lato", Arial, sans-serif;
  }
  .stage { position: relative; width: 1200px; height: 926px; }

  .card {
    position: absolute; left: 250px; width: 700px; height: 400px;
    background: radial-gradient(ellipse at 45% 35%, var(--card-black-light) 0%, var(--card-black) 70%);
    box-shadow: 0 10px 24px rgba(0,0,0,.28);
    overflow: hidden;
  }
  .card--back { top: 42px; }
  .card--front { top: 484px; }

  /* Back side */
  .back-brand {
    position: absolute; top: 140px; left: 0; right: 0;
    text-align: center;
    color: var(--brand-blue-bright);
    font-weight: 900; font-size: 34px; letter-spacing: 1px;
    text-transform: uppercase;
  }
  .back-website {
    position: absolute; top: 236px; left: 0; right: 0;
    text-align: center;
    color: var(--grey);
    font-size: 15px; letter-spacing: 7px; text-transform: uppercase;
  }

  /* Front side */
  .front-brand {
    position: absolute; top: 38px; left: 48px;
    color: var(--brand-blue-bright);
    font-weight: 900; font-size: 19px; letter-spacing: .5px;
    text-transform: uppercase;
  }
  .person-name {
    position: absolute; top: 84px; left: 48px;
    color: var(--brand-blue-bright);
    font-size: 30px; font-weight: 400; text-transform: uppercase;
  }
  .person-name strong { font-weight: 700; }
  .contact-list {
    position: absolute; top: 136px; left: 48px;
    list-style: none;
  }
  .contact-list li {
    display: flex; align-items: center; gap: 12px;
    color: var(--text-light);
    font-size: 17px; line-height: 29px; letter-spacing: .4px;
  }
  .contact-list svg { width: 16px; height: 16px; fill: none; stroke: var(--text-light); stroke-width: 1.6; flex: none; }

  .address-band {
    position: absolute; left: 0; right: 0; bottom: 0; height: 84px;
    background: var(--brand-blue);
    display: flex; align-items: center; padding-left: 48px;
    color: var(--white);
    font-weight: 700; font-size: 19px; letter-spacing: .6px;
    text-transform: uppercase;
  }
</style>
</head>
<body>
<main class="stage">

  <section class="card card--back" aria-label="Business card back">
    <p class="back-brand">Harbor Lane Freightworks, LLC</p>
    <p class="back-website">www.harborlanefreight.com</p>
  </section>

  <section class="card card--front" aria-label="Business card front">
    <p class="front-brand">Harbor Lane Freightworks, LLC</p>
    <h1 class="person-name">Daniel <strong>Reyes</strong></h1>
    <ul class="contact-list">
      <li>
        <svg viewBox="0 0 16 16" aria-hidden="true"><rect x="4" y="1" width="8" height="14" rx="1.5"/><line x1="7" y1="12.5" x2="9" y2="12.5"/></svg>
        555-201-4730
      </li>
      <li>
        <svg viewBox="0 0 16 16" aria-hidden="true"><path d="M2 6c0-2 3-3 6-3s6 1 6 3l-2 1-1-2H5L4 7z"/><rect x="3" y="8" width="10" height="6" rx="1"/></svg>
        555-201-4731
      </li>
      <li>
        <svg viewBox="0 0 16 16" aria-hidden="true"><rect x="4" y="1.5" width="8" height="5"/><rect x="2" y="6.5" width="12" height="6" rx="1"/><rect x="4" y="10" width="8" height="4.5"/></svg>
        555-201-4732
      </li>
      <li>
        <svg viewBox="0 0 16 16" aria-hidden="true"><rect x="1.5" y="3.5" width="13" height="9" rx="1"/><path d="M1.5 4l6.5 5 6.5-5"/></svg>
        dreyes@harborlanefreight.com
      </li>
      <li>
        <svg viewBox="0 0 16 16" aria-hidden="true"><path d="M7 9l2-2"/><path d="M6 7.5L3.5 10a2 2 0 0 0 2.8 2.8L8.5 10.5"/><path d="M10 8.5l2.5-2.5a2 2 0 0 0-2.8-2.8L7.5 5.5"/></svg>
        www.harborlanefreight.com
      </li>
    </ul>
    <p class="address-band">418 Dockside Road, Unit #12, Pier Bldg, OR 97204</p>
  </section>

</main>
</body>
</html>
```